Larkspur Ridge Management - Business Cards

I need business cards. My current logo was designed by a designer at this site and I very much like and am happy with the results. I would like a business card that is trendy, unique, current yet professional. I deal with high net worth clients daily

Target Market(s)

Out of state investors looking to get into the rental market in Ohio

Industry/Entity Type

Property Management, Consulting

Contact Information for Business Card

Name, Title (Chief Financial Officer) office phone number (555) 817-3094 website address larkridgemgmt.example

Font styles to use
Sans Serif

Colors
0054AA
0677BA
7BADD7
CADEEF
E8F1F8
0094D4
00A9DD
6FCCEA
C7EBF8
E9F6FB
00AB8E
00BBA5
67D7C9
C6EFE9
E9F9F6

```html
<!DOCTYPE html>
<html lang="en">
<head>
<meta charset="utf-8">
<title>Larkspur Ridge Management – Business Card</title>
<link href="https://fonts.googleapis.com/css2?family=Montserrat:wght@400;500;800&family=Open+Sans:wght@700&display=swap" rel="stylesheet">
<style>
  :root {
    --blue: #0054AA;
    --blue-mid: #0677BA;
    --cyan: #0094D4;
    --teal: #00AB8E;
    --teal-bright: #00BBA5;
    --mist: #E8F1F8;
    --ink: #1c2a3a;
    --paper: #ffffff;
    --stage: #E9F6FB;
  }
  * { box-sizing: border-box; margin: 0; padding: 0; }
  html, body { width: 1200px; height: 1200px; overflow: hidden; }
  body {
    background: var(--stage);
    font-family: "Montserrat", sans-serif;
    display: flex;
    align-items: center;
    justify-content: center;
    gap: 80px;
  }
  .card {
    position: relative;
    width: 420px;
    height: 700px;
    border-radius: 30px;
    overflow: hidden;
    box-shadow: 0 10px 30px rgba(0, 84, 170, 0.18);
  }
  .card--front { background: var(--paper); color: var(--ink); }
  .card--back { background: var(--blue); color: #fff; }

  .card__tab {
    position: absolute;
    bottom: 0;
    left: 50%;
    transform: translateX(-50%);
    width: 62%;
    height: 26px;
    border-radius: 10px 10px 0 0;
  }
  .card--front .card__tab { background: var(--cyan); }
  .card--back .card__tab { background: var(--teal); }

  .brand {
    display: flex;
    align-items: center;
    justify-content: center;
    gap: 14px;
    font-family: "Montserrat", sans-serif;
    font-weight: 800;
    text-transform: uppercase;
    line-height: 1.08;
    letter-spacing: 0.5px;
    font-size: 30px;
  }
  .brand__dot {
    flex: none;
    width: 34px;
    height: 34px;
    border-radius: 50%;
  }
  .card--front .brand { position: absolute; top: 150px; left: 0; right: 0; color: var(--blue); }
  .card--front .brand__dot { background: var(--teal); }
  .card--back .brand { position: absolute; top: 290px; left: 0; right: 0; color: #fff; }
  .card--back .brand__dot { background: var(--teal-bright); }

  .person {
    position: absolute;
    top: 362px;
    left: 0; right: 0;
    text-align: center;
  }
  .person__name {
    font-weight: 800;
    font-size: 31px;
    letter-spacing: 1px;
    color: var(--blue);
    text-transform: uppercase;
  }
  .person__title {
    margin-top: 6px;
    font-size: 20px;
    color: var(--cyan);
    letter-spacing: 0.5px;
  }
  .address {
    margin-top: 28px;
    font-size: 17px;
    line-height: 1.45;
    letter-spacing: 0.5px;
  }
  .icons {
    display: flex;
    justify-content: center;
    gap: 12px;
    margin-top: 26px;
  }
  .icon {
    width: 38px; height: 38px;
    border-radius: 50%;
    display: flex; align-items: center; justify-content: center;
  }
  .icon--accent { background: var(--cyan); }
  .icon--primary { background: var(--blue); }
  .contact {
    margin-top: 18px;
    font-size: 16px;
    line-height: 1.55;
    letter-spacing: 0.6px;
  }
  .back__url {
    position: absolute;
    bottom: 90px;
    left: 0; right: 0;
    text-align: center;
    font-family: "Open Sans", sans-serif;
    font-weight: 700;
    font-size: 15px;
    letter-spacing: 4px;
  }
</style>
</head>
<body>
  <section class="card card--front">
    <div class="brand">
      <span class="brand__dot"></span>
      <span class="brand__name">Larkspur Ridge<br>Management</span>
    </div>
    <div class="person">
      <h1 class="person__name">Dana Whitfield</h1>
      <p class="person__title">Chief Financial Officer</p>
      <p class="address">48 Alder Crossing Road<br>Columbus, OH 43215</p>
      <div class="icons">
        <span class="icon icon--accent">
          <svg width="18" height="18" viewBox="0 0 24 24" fill="#fff"><path d="M6.6 10.8a15.1 15.1 0 0 0 6.6 6.6l2.2-2.2a1 1 0 0 1 1-.25 11.4 11.4 0 0 0 3.6.57 1 1 0 0 1 1 1V20a1 1 0 0 1-1 1A17 17 0 0 1 3 4a1 1 0 0 1 1-1h3.5a1 1 0 0 1 1 1c0 1.25.2 2.45.57 3.57a1 1 0 0 1-.25 1z"/></svg>
        </span>
        <span class="icon icon--primary">
          <svg width="20" height="20" viewBox="0 0 24 24" fill="none" stroke="#fff" stroke-width="1.8"><rect x="3" y="6" width="18" height="13" rx="1.5"/><path d="M3 7l9 7 9-7"/></svg>
        </span>
        <span class="icon icon--accent">
          <svg width="20" height="20" viewBox="0 0 24 24" fill="none" stroke="#fff" stroke-width="1.5"><circle cx="12" cy="12" r="9"/><ellipse cx="12" cy="12" rx="4" ry="9"/><path d="M3 12h18M5 7h14M5 17h14"/></svg>
        </span>
      </div>
      <p class="contact">(555) 817-3094<br>dana@larkridgemgmt.example<br>www.larkridgemgmt.example</p>
    </div>
    <div class="card__tab"></div>
  </section>

  <section class="card card--back">
    <div class="brand">
      <span class="brand__dot"></span>
      <span class="brand__name">Larkspur Ridge<br>Management</span>
    </div>
    <p class="back__url">www.larkridgemgmt.example</p>
    <div class="card__tab"></div>
  </section>
</body>
</html>
```